Design a business card for Lantern Webpage

I need a business card designed for a new company called LanternWebpage.example . I will be doing a lot of networking and the business card is the first thing people will see. I need to get them to my website. I already have a logo and attached it here.
A Lantern Webpage is a personal website with career tools to promote your professional success. For more information, visit LanternWebpage.example .

My tag line is Stride Ahead-and Thrive although if there is room, I would rather use - Don't leave your career up to someone else. Stride Ahead-and Thrive.

My target customer is the professional who is successful at their job but needs to get to the next level in their career. Essentially, everyone on Careerloop.example that does not own their own company.

Other information for the card:

Marcus Delbrook
CEO

555-014-7732

Marcus@LanternWebpage.example

LanternWebpage.example

I need a high resolution deign ready to print. I also need the original PSD files.

Target Market(s)

Professionals in the growth phase of their career

Industry/Entity Type

Business

Contact Information for Business Card

Logo

Don't leave your career up to someone else. Stride Ahead-and Thrive.

Marcus Delbrook
CEO

555-014-7732

Marcus@LanternWebpage.example

LanternWebpage.example

Font styles to use
Serif

Requirements
Must have
• My log and original colors, Images and it has to be fun and very impressive

```html
<!DOCTYPE html>
<html lang="en">
<head>
<meta charset="utf-8">
<title>Lantern Webpage – Business Card</title>
<link rel="stylesheet" href="https://fonts.googleapis.com/css2?family=Lora:wght@400;500;700&display=swap">
<style>
  :root {
    --page-bg: #e9e9ea;
    --card-white: #f7f7f7;
    --slate: #3a4752;
    --maroon: #7e2a40;
    --ink: #2f3a44;
    --ink-soft: #55606a;
    --on-slate: #ffffff;
  }
  html, body {
    margin: 0;
    padding: 0;
    width: 1200px;
    height: 900px;
    overflow: hidden;
    background: var(--page-bg);
    font-family: "Lora", serif;
  }
  .canvas {
    position: relative;
    width: 1200px;
    height: 900px;
  }
  .card {
    position: absolute;
    left: 270px;
    width: 660px;
    height: 377px;
    border-radius: 28px;
    background: var(--card-white);
    overflow: hidden;
    box-shadow: 0 6px 18px rgba(0,0,0,0.15);
  }
  .card--front { top: 50px; }
  .card--back { top: 473px; }
  .card__shapes {
    position: absolute;
    inset: 0;
    width: 660px;
    height: 377px;
  }
  .brand {
    position: absolute;
    display: flex;
    align-items: center;
    gap: 10px;
    color: var(--ink);
    font-weight: 700;
    letter-spacing: 2px;
    text-transform: uppercase;
    line-height: 1;
    white-space: nowrap;
  }
  .brand__dot {
    width: 14px;
    height: 14px;
    border-radius: 50%;
    background: var(--maroon);
    flex: none;
  }
  .card--front .brand { left: 40px; top: 48px; font-size: 28px; }
  .card--back .brand { left: 50%; top: 50%; transform: translate(-50%, -50%); font-size: 40px; gap: 14px; }
  .card--back .brand__dot { width: 20px; height: 20px; }
  .person {
    position: absolute;
    right: 40px;
    top: 92px;
    text-align: right;
    color: var(--ink);
  }
  .person__name {
    margin: 0;
    font-size: 22px;
    font-weight: 500;
    letter-spacing: 2px;
    text-transform: uppercase;
  }
  .person__role {
    margin: 2px 0 0;
    font-size: 14px;
    color: var(--ink-soft);
  }
  .contacts {
    position: absolute;
    right: 40px;
    top: 262px;
    margin: 0;
    padding: 0;
    list-style: none;
    color: var(--on-slate);
    font-size: 13px;
    letter-spacing: 0.5px;
  }
  .contacts li {
    display: flex;
    justify-content: flex-end;
    align-items: center;
    gap: 8px;
    height: 21px;
  }
  .contacts svg { width: 12px; height: 12px; fill: none; stroke: var(--on-slate); stroke-width: 1.6; }
  .tagline {
    position: absolute;
    left: 40px;
    bottom: 22px;
    margin: 0;
    color: var(--on-slate);
    font-size: 13px;
    font-style: italic;
    letter-spacing: 0.5px;
  }
</style>
</head>
<body>
<main class="canvas">
  <section class="card card--front" aria-label="Business card front">
    <svg class="card__shapes" viewBox="0 0 660 377" aria-hidden="true">
      <path d="M0,158 C200,133 480,153 660,233 L660,241 C480,161 200,141 0,166 Z" fill="var(--maroon)"/>
      <path d="M0,175 C200,150 480,170 660,250 L660,377 L0,377 Z" fill="var(--slate)"/>
    </svg>
    <div class="brand"><span class="brand__dot"></span>Lantern Webpage</div>
    <div class="person">
      <p class="person__name">Marcus Delbrook</p>
      <p class="person__role">CEO</p>
    </div>
    <ul class="contacts">
      <li>555-014-7732
        <svg viewBox="0 0 12 12"><path d="M2 1.5 L4.5 1.5 L5.2 4 L3.8 5 C4.5 6.6 5.4 7.5 7 8.2 L8 6.8 L10.5 7.5 L10.5 10 C6 10.5 1.5 6 2 1.5 Z"/></svg></li>
      <li>Marcus@LanternWebpage.example
        <svg viewBox="0 0 12 12"><rect x="1" y="2.5" width="10" height="7" rx="0.8"/><path d="M1.3 3 L6 6.6 L10.7 3"/></svg></li>
      <li>LanternWebpage.example
        <svg viewBox="0 0 12 12"><circle cx="6" cy="6" r="4.8"/><path d="M1.2 6 H10.8 M6 1.2 C3.8 4 3.8 8 6 10.8 M6 1.2 C8.2 4 8.2 8 6 10.8"/></svg></li>
    </ul>
    <p class="tagline">Don't leave your career up to someone else. Stride Ahead-and Thrive.</p>
  </section>

  <section class="card card--back" aria-label="Business card back">
    <div class="brand"><span class="brand__dot"></span>Lantern Webpage</div>
  </section>
</main>
</body>
</html>
```